halbrook paving works

Needs to have phone number 0418352790 and email carlwhitby@mailnest.com.au.
ABN 27813046652
name carl whitby

For all your concreting solutions
Excavation
Exposed & colour concrete
House & shed slabs
Driveways
Landing & steps

Contact Information for Business Card

ph 0418352790
email carlwhitby@mailnest.com.au.
ABN 27813046652
name carl whitby

```html
<!DOCTYPE html>
<html lang="en">
<head>
<meta charset="utf-8">
<title>Halbrook Paving Works – Business Cards</title>
<link rel="stylesheet" href="https://fonts.googleapis.com/css2?family=Montserrat:wght@500;600&family=Roboto:ital,wght@0,400;1,400&display=swap">
<style>
  :root {
    --bg: #2b2e33;
    --card: #141414;
    --card-soft: #1e1e1e;
    --orange: #f36f21;
    --grey: #8a8a8a;
    --white: #e8e8e8;
  }
  html, body {
    margin: 0;
    width: 1200px;
    height: 900px;
    overflow: hidden;
    background: var(--bg);
  }
  .canvas {
    position: relative;
    width: 1200px;
    height: 900px;
  }
  .card {
    position: absolute;
    width: 560px;
    height: 320px;
    border-radius: 18px;
    overflow: hidden;
    background: radial-gradient(ellipse at 40% 30%, var(--card-soft), var(--card) 70%);
    box-shadow: 0 10px 30px rgba(0,0,0,.45);
    font-family: "Roboto", Arial, sans-serif;
    color: var(--white);
  }
  .card-edge {
    position: absolute;
    left: 0; bottom: 0;
    width: 100%; height: 26px;
  }
  /* Company side */
  .card-company { left: 580px; top: 110px; }
  .brand-mark {
    position: absolute;
    left: 70px; top: 58px;
    width: 70px; height: 70px;
    background: var(--orange);
  }
  .brand-divider {
    position: absolute;
    left: 172px; top: 36px;
    width: 2px; height: 112px;
    background: var(--orange);
  }
  .brand-name {
    position: absolute;
    left: 192px; top: 42px;
    width: 340px;
    font-family: "Montserrat", Arial, sans-serif;
    font-weight: 600;
    color: var(--orange);
    text-transform: uppercase;
  }
  .brand-line1 { font-size: 26px; letter-spacing: .5px; line-height: 32px; }
  .brand-line2 {
    display: flex; align-items: center; gap: 10px;
    font-size: 20px; letter-spacing: 4px; line-height: 26px;
  }
  .brand-line2::before, .brand-line2::after {
    content: ""; flex: 1; height: 2px; background: var(--grey);
  }
  .brand-phone {
    position: absolute;
    left: 192px; top: 104px;
    width: 340px;
    text-align: center;
    font-size: 22px;
    letter-spacing: 3px;
    color: var(--orange);
  }
  .tagline {
    position: absolute;
    left: 0; top: 178px; width: 100%;
    text-align: center;
    font-style: italic;
    font-size: 17px;
    color: var(--orange);
  }
  .services {
    position: absolute;
    left: 0; top: 204px; width: 100%;
    text-align: center;
    font-size: 14.5px;
    line-height: 22px;
    color: var(--white);
  }
  /* Personal side */
  .card-person { left: 60px; top: 470px; }
  .person-name {
    position: absolute;
    left: 0; top: 34px; width: 100%;
    text-align: center;
    font-family: "Montserrat", Arial, sans-serif;
    font-weight: 600;
    font-size: 32px;
    letter-spacing: 1px;
    color: var(--orange);
    text-transform: uppercase;
  }
  .person-mark {
    position: absolute;
    left: 254px; top: 96px;
    width: 52px; height: 52px;
    background: var(--grey);
  }
  .contact {
    position: absolute;
    left: 0; top: 166px; width: 100%;
    text-align: center;
    font-size: 19px;
    line-height: 27px;
  }
  .contact .abn { color: var(--orange); }
</style>
</head>
<body>
<div class="canvas">

  <section class="card card-company">
    <div class="brand-mark"></div>
    <div class="brand-divider"></div>
    <div class="brand-name">
      <div class="brand-line1">Halbrook Paving</div>
      <div class="brand-line2">Works</div>
    </div>
    <div class="brand-phone">0418352790</div>
    <p class="tagline" style="margin:0">For all your Concreting Solutions</p>
    <p class="services" style="margin:0">
      Excavation | Exposed &amp; Colour Concrete | House &amp; Shed Slabs<br>
      Driveways | Landing &amp; Steps
    </p>
    <svg class="card-edge" viewBox="0 0 560 26" preserveAspectRatio="none" aria-hidden="true">
      <path d="M0 12 H270 L280 0 L290 12 H560 V26 H0 Z" fill="#f36f21"/>
    </svg>
  </section>

  <section class="card card-person">
    <h1 class="person-name" style="margin:0">Carl Whitby</h1>
    <div class="person-mark"></div>
    <div class="contact">
      <div class="phone">041 835 2790</div>
      <div class="email">carlwhitby@mailnest.com.au</div>
      <div class="abn">ABN 27813046652</div>
    </div>
    <svg class="card-edge" viewBox="0 0 560 26" preserveAspectRatio="none" aria-hidden="true">
      <path d="M0 12 H270 L280 0 L290 12 H560 V26 H0 Z" fill="#f36f21"/>
    </svg>
  </section>

</div>
</body>
</html>
```